Hong Kong residential leasing and sales company needs a website design

Hong Kong has many competitive real estate agents. The majority of us have the same listings so, besides the team and experience, a website is what makes us stand out. A first impression. We need our website to be user friendly, informative and to have a wow factor. Most sites are generic so whilst we are close to accepting that maybe that's the only formula which works....we would like to see if we're missing something! Our clients are a mix of International users of all ages but probably ultimately 35+.. We have a logo (attached) which we would like to keep - designed by artmarketly. Flexible with colours except red.
examples of our competitors are:
http://www.brindlewoodestates.example
http://www.nuvo.example/home
http://www.premierdwellingsvx.example
http://www.orchid-lettings.example
http://www.tidemark-harrowgates.example
We were thinking of having the following in a menu bar with drop downs for most...some more than others. Home / For Sale / For Rent / Property 101 / About us / Contact Us ..
Look forward to seeing your ideas. Thanks in advance.

```html
<!DOCTYPE html>
<html lang="en">
<head>
<meta charset="utf-8">
<title>Lumen Residences – Home</title>
<link href="https://fonts.googleapis.com/css2?family=Crimson+Text:wght@400;600&display=swap" rel="stylesheet">
<style>
:root{
  --purple:#7d3aa6;
  --purple-light:#8e44b5;
  --lilac:#cba7dc;
  --ink:#1c1c1c;
  --text:#333;
  --muted:#666;
  --rule:#e2e2e2;
  --panel:#f3f3f3;
  --fb:#3b5998;
  --social:#c9c9c9;
}
*{box-sizing:border-box;margin:0;padding:0}
html,body{width:1200px;height:958px;overflow:hidden;background:#fff}
body{position:relative;font-family:"Crimson Text",Georgia,serif;color:var(--text)}
a{color:inherit;text-decoration:none}

.brand{position:absolute;display:flex;align-items:center;gap:10px;font-weight:400;color:var(--ink)}
.brand-mark{width:22px;height:22px;background:var(--purple)}
.brand--header{left:112px;top:58px;font-size:31px;letter-spacing:1px}
.brand--footer{left:0;right:0;top:752px;justify-content:center;font-size:29px}

.utility{position:absolute;left:747px;top:-2px;width:341px;height:38px;border:1px solid #d6d6d6;border-top:none;border-radius:0 0 6px 6px;box-shadow:0 2px 4px rgba(0,0,0,.15);background:#fff;font-size:13px;display:flex;align-items:center;padding-left:9px}
.currency-label{font-family:Arial,sans-serif;font-size:12px;color:#000}
.currency-select{margin-left:6px;width:78px;height:22px;border:1px solid #aaa;font-family:Arial,sans-serif;font-size:11px;display:flex;align-items:center;padding-left:3px;position:relative}
.currency-select::after{content:"";position:absolute;right:1px;top:1px;width:16px;height:18px;border:1px solid #888;background:linear-gradient(#fafafa,#ddd)}
.currency-select span.arrow{position:absolute;right:5px;top:8px;border:4px solid transparent;border-top:5px solid #000;z-index:1}
.lang{margin-left:38px;display:flex;gap:9px;color:#444;font-size:13px}
.lang .sep{color:var(--purple)}
.lang .active{border-bottom:2px solid #b0243a;padding-bottom:1px}

.main-nav{position:absolute;top:86px;right:118px;display:flex;font-size:17px;color:var(--ink)}
.main-nav a{padding:5px 10px 6px;line-height:20px}
.main-nav a.current{background:var(--purple);color:#fff}

.hero{position:absolute;left:109px;top:161px;width:644px;height:499px;border:1px solid #d4d4d4;overflow:hidden;
  background:linear-gradient(180deg,#f2f1ee 0%,#ecebe7 30%,#c9dbe6 52%,#9bb5c2 62%,#6b7371 75%,#d9d8d4 90%,#e8e6e2 100%)}
.search-tabs{position:absolute;left:24px;top:13px;display:flex;gap:8px;font-size:18px;color:var(--ink)}
.search-tabs span{padding:10px 20px 0;height:37px}
.search-tabs .on{background:rgba(255,255,255,.85)}
.search-tabs .off{background:#fff}
.search-panel{position:absolute;left:24px;top:50px;width:594px;height:98px;background:rgba(255,255,255,.85)}
.area-select{position:absolute;left:24px;top:23px;width:436px;height:33px;background:#fff;border:1px solid #c7c7c7;font-size:18px;color:#999;padding:3px 15px}
.area-select::after{content:"";position:absolute;right:10px;top:13px;border:5px solid transparent;border-top:6px solid var(--purple)}
.search-btn{position:absolute;left:466px;top:23px;width:101px;height:32px;background:var(--purple);color:#fff;font-size:18px;text-align:center;line-height:31px}
.count{position:absolute;left:30px;top:62px;font-size:12px;color:#333}
.advanced{position:absolute;right:26px;top:66px;font-size:12px;color:var(--purple)}
.advanced::after{content:"";display:inline-block;margin-left:6px;border:4px solid transparent;border-top:5px solid var(--purple);vertical-align:-1px}
.caption{position:absolute;left:0;right:0;top:394px;height:50px;background:rgba(40,40,40,.75);color:#fff;font-size:21px;padding:10px 53px}
.thumbs{position:absolute;left:246px;top:617px;display:flex;gap:10px}
.thumb{width:85px;height:70px;border:1px solid #fff}
.t1{background:linear-gradient(#c9d3cf,#7a8c85 60%,#e9e7e2)}
.t2{background:linear-gradient(#eee,#b9cbd6 55%,#6f6a63)}
.t3{background:linear-gradient(#d8d6d3,#8d8a86 55%,#4b4845)}
.t4{background:linear-gradient(#d6c29a,#9a7d4c 55%,#e4d6b5)}

.featured-title{position:absolute;left:769px;top:155px;font-size:26px;color:var(--purple-light);font-weight:400}
.listings{position:absolute;left:763px;top:199px;width:337px;list-style:none}
.listing{position:relative;height:93px;display:flex}
.listing.highlight{background:var(--panel)}
.listing-photo{width:97px;height:88px;flex:none}
.p1{background:linear-gradient(135deg,#2a3a55,#7fa4c7 50%,#1b1b1b)}
.p2{background:linear-gradient(135deg,#1d1410,#8a5a32 50%,#2b201a)}
.p3{background:linear-gradient(135deg,#6b5a6e,#b58a5a 50%,#3a2a22)}
.p4{background:linear-gradient(180deg,#f2efe8,#b4a890 55%,#4f7a32)}
.p5{background:linear-gradient(135deg,#d8dcdc,#9ea4a6 50%,#eceeee)}
.listing-info{padding:3px 0 0 15px;font-size:16.5px;line-height:25.5px;color:var(--text)}
.listing-name{color:var(--purple-light)}
.ribbon{position:absolute;right:0;top:4px;width:34px;height:83px}
.ribbon-label{position:absolute;right:8px;top:12px;writing-mode:vertical-rl;transform:rotate(180deg);color:#fff;font-size:14px}
.more{position:absolute;left:1006px;top:668px;font-size:19px;color:var(--ink)}
.more::after{content:"";display:inline-block;margin-left:13px;border:5px solid transparent;border-left:6px solid var(--purple);vertical-align:0}

.rule{position:absolute;left:0;right:0;height:1px;background:var(--rule)}
.footer-nav{position:absolute;left:0;right:0;top:824px;display:flex;justify-content:center;gap:20px;font-size:17px;color:var(--ink)}
.social{position:absolute;left:512px;top:857px;display:flex;gap:10px}
.social span{width:30px;height:30px;border-radius:50%;background:var(--social)}
.social span.dark{background:var(--fb)}
.social svg{display:block}
.legal{position:absolute;left:0;right:0;top:894px;text-align:center;font-size:17px;color:var(--ink)}
.copyright{position:absolute;left:0;right:0;top:922px;text-align:center;font-size:16px;color:var(--ink)}
</style>
</head>
<body>

<header>
  <div class="brand brand--header"><span class="brand-mark"></span>Lumen Residences</div>

  <div class="utility">
    <span class="currency-label">Currency:</span>
    <span class="currency-select">HKD<span class="arrow"></span></span>
    <span class="lang"><span>简体</span><span class="sep">|</span><span>繁体</span><span class="sep">|</span><span class="active">English</span></span>
  </div>

  <nav class="main-nav">
    <a class="current" href="#">Home</a>
    <a href="#">For Sale</a>
    <a href="#">For Rent</a>
    <a href="#">Property 101</a>
    <a href="#">About us</a>
    <a href="#">Contact Us</a>
  </nav>
</header>

<main>
  <section class="hero" role="img" aria-label="Bright white living room with draped curtains opening onto a sea view">
    <div class="search-tabs"><span class="on">For Sale</span><span class="off">For Rent</span></div>
    <div class="search-panel">
      <div class="area-select">Select your area</div>
      <div class="search-btn">Search</div>
      <div class="count">3,258,045 Properties in HongKong</div>
      <div class="advanced">Advanced Search</div>
    </div>
    <div class="caption">Tai Lam Crescent, Sai Kung, HONG KONG</div>
  </section>
  <div class="thumbs">
    <div class="thumb t1" role="img" aria-label="Lounge with white sofa"></div>
    <div class="thumb t2" role="img" aria-label="Living room with curtains and sea view"></div>
    <div class="thumb t3" role="img" aria-label="Study with bookshelves"></div>
    <div class="thumb t4" role="img" aria-label="Warm lit dining area"></div>
  </div>

  <h2 class="featured-title">Featured Properties</h2>
  <ul class="listings">
    <li class="listing highlight">
      <div class="listing-photo p1" role="img" aria-label="Modern staircase interior"></div>
      <div class="listing-info"><div class="listing-name">CUM SOLUTA NOBIS</div><div>HKD 35 M</div><div>Mid levels east</div></div>
      <svg class="ribbon" viewBox="0 0 34 83"><polygon points="0,0 34,0 34,83 14,67 0,67" fill="#cba7dc"/></svg>
      <span class="ribbon-label">For Sale</span>
    </li>
    <li class="listing">
      <div class="listing-photo p2" role="img" aria-label="Dark wood dining room"></div>
      <div class="listing-info"><div class="listing-name">CUM SOLUTA NOBIS</div><div>HKD 35 M</div><div>Mid levels east</div></div>
    </li>
    <li class="listing">
      <div class="listing-photo p3" role="img" aria-label="Living room with city view at dusk"></div>
      <div class="listing-info"><div class="listing-name">CUM SOLUTA NOBIS</div><div>HKD 35 M</div><div>Mid levels east</div></div>
    </li>
    <li class="listing">
      <div class="listing-photo p4" role="img" aria-label="Modern house exterior with lawn"></div>
      <div class="listing-info"><div class="listing-name">CUM SOLUTA NOBIS</div><div>HKD 35 M</div><div>Mid levels east</div></div>
    </li>
    <li class="listing">
      <div class="listing-photo p5" role="img" aria-label="Bright white bathroom"></div>
      <div class="listing-info"><div class="listing-name">CUM SOLUTA NOBIS</div><div>HKD 35 M</div><div>Mid levels east</div></div>
    </li>
  </ul>
  <a class="more" href="#">More</a>
</main>

<footer>
  <div class="rule" style="top:711px"></div>
  <div class="brand brand--footer"><span class="brand-mark"></span>Lumen Residences</div>
  <div class="rule" style="top:815px"></div>
  <nav class="footer-nav">
    <a href="#">Home</a><a href="#">For Sale</a><a href="#">For Rent</a><a href="#">Property 101</a><a href="#">About us</a><a href="#">Contact Us</a>
  </nav>
  <div class="rule" style="top:852px"></div>
  <div class="social">
    <span></span>
    <span class="dark"></span>
    <span></span>
    <span></span>
    <span><svg width="30" height="30" viewBox="0 0 30 30"><rect x="8" y="10" width="14" height="10" fill="none" stroke="#fff" stroke-width="1.6"/><polyline points="8,10 15,16 22,10" fill="none" stroke="#fff" stroke-width="1.6"/></svg></span>
  </div>
  <div class="legal">Terms &amp; Conditions&nbsp;|&nbsp; Privacy Policy</div>
  <div class="copyright">© 2014.www.companyname.com</div>
  <div class="rule" style="top:954px"></div>
</footer>

</body>
</html>
```